Bastion Guard Services

Our Company is a security business which needs a cut edge design, the final product should have all relevant information and maintain a bold but modern and professional look.

Target Market(s)

A cut edge design which will attract any audience

Industry/Entity Type

Security

Contact Information for Business Card

BASTION GUARD SERVICES

Daniel Kowalski
Operations Manager
Phone: 0419 357 216

Email: info@bastionguardex.com.au
Web: www.bastionguardex.com.au

Requirements
Must have
• Must be double sided and contain all relevant information and the company logo.

```html
<!DOCTYPE html>
<html lang="en">
<head>
<meta charset="utf-8">
<title>Bastion Guard Services – Business Card</title>
<link rel="stylesheet" href="https://fonts.googleapis.com/css2?family=Play:wght@400;700&display=swap">
<style>
  :root {
    --teal: #1f4a4f;
    --teal-light: #3b6b70;
    --orange: #f08a1c;
    --ink: #2b2f31;
    --card: #ffffff;
    --backdrop: #e9e7e3;
  }
  * { margin: 0; padding: 0; box-sizing: border-box; }
  html, body { width: 1200px; height: 790px; overflow: hidden; }
  body {
    background: var(--backdrop);
    font-family: "Play", sans-serif;
    display: flex;
    flex-direction: column;
    align-items: center;
    justify-content: center;
    gap: 34px;
  }
  .card {
    position: relative;
    width: 640px;
    height: 360px;
    background: var(--card);
    box-shadow: 0 6px 18px rgba(0,0,0,0.18);
    overflow: hidden;
  }
  /* Back side */
  .back .bar-top {
    position: absolute; top: 22px; right: 0;
    width: 160px; height: 24px; background: var(--teal);
  }
  .back .bar-left {
    position: absolute; top: 120px; left: 0;
    width: 150px; height: 24px; background: var(--teal);
  }
  .back .brand {
    position: absolute; left: 0; right: 0; top: 160px;
    display: flex; align-items: center; justify-content: center; gap: 18px;
  }
  .back .brand-mark { width: 34px; height: 34px; background: var(--orange); }
  .back .brand-name {
    font-weight: 700; font-size: 48px; letter-spacing: 2px; color: var(--teal);
  }
  /* Front side */
  .front .band {
    position: absolute; top: 30px; left: 150px; right: 0;
    height: 26px; background: var(--teal);
    border-top: 3px solid #d9e0e1;
    color: #dfe7e8; font-size: 15px; letter-spacing: 0.5px;
    line-height: 23px; padding-left: 14px; text-transform: uppercase;
  }
  .front .brand {
    position: absolute; left: 40px; top: 160px;
    display: flex; align-items: center; gap: 12px;
  }
  .front .brand-mark { width: 24px; height: 24px; background: var(--orange); }
  .front .brand-name {
    font-weight: 700; font-size: 30px; letter-spacing: 1px; color: var(--teal);
  }
  .front .person { position: absolute; left: 350px; top: 118px; }
  .front .person-name { font-size: 27px; color: var(--teal); line-height: 1; }
  .front .person-role { font-size: 15px; color: var(--orange); margin-top: 4px; }
  .front .contacts {
    position: absolute; left: 350px; top: 200px;
    list-style: none; font-size: 16px; color: var(--ink);
  }
  .front .contacts li {
    display: flex; align-items: center; gap: 14px; height: 30px;
  }
  .front .contacts svg { width: 18px; height: 18px; flex: none; }
</style>
</head>
<body>
  <section class="card back" aria-label="Card back">
    <div class="bar-top"></div>
    <div class="bar-left"></div>
    <div class="brand">
      <span class="brand-mark"></span>
      <span class="brand-name">BASTION GUARD</span>
    </div>
  </section>

  <section class="card front" aria-label="Card front">
    <div class="band">Bastion Guard Services</div>
    <div class="brand">
      <span class="brand-mark"></span>
      <span class="brand-name">BASTION GUARD</span>
    </div>
    <div class="person">
      <p class="person-name">Daniel Kowalski</p>
      <p class="person-role">Operations Manager</p>
    </div>
    <ul class="contacts">
      <li>
        <svg viewBox="0 0 18 18" aria-hidden="true"><rect x="4" y="1" width="10" height="16" rx="2" fill="var(--orange)"/><rect x="6" y="3.5" width="6" height="9" fill="#fff"/><circle cx="9" cy="14.6" r="1" fill="#fff"/></svg>
        <span>0419 357 216</span>
      </li>
      <li>
        <svg viewBox="0 0 18 18" aria-hidden="true"><rect x="1" y="4" width="16" height="11" fill="var(--orange)"/><path d="M1 4 L9 10.5 L17 4" fill="none" stroke="#fff" stroke-width="1.4"/></svg>
        <span>info@bastionguardex.com.au</span>
      </li>
      <li>
        <svg viewBox="0 0 18 18" aria-hidden="true"><circle cx="9" cy="9" r="7.5" fill="none" stroke="var(--orange)" stroke-width="1.6"/><ellipse cx="9" cy="9" rx="3.2" ry="7.5" fill="none" stroke="var(--orange)" stroke-width="1.3"/><path d="M1.5 9 H16.5 M3 5 H15 M3 13 H15" stroke="var(--orange)" stroke-width="1.2"/></svg>
        <span>www.bastionguardex.com.au</span>
      </li>
    </ul>
  </section>
</body>
</html>
```